BLAC inc Business Card Design

I have a rough draft of the BLAC inc logo that I would like to use on the business card. I also attached our logo for Quillbrook.com. I also included a sample of a business card from another mortgage company that I like. We would like a tagline on the back to say "let's get started" and below Quillbrook.com
Contact Information for Business Card
Brightway Lending and Capital, inc
Marcus Delane
Mortgage Specialist
Direct (555)204-1187
Cell (555)318-4592
Fax (555)907-2263
marcus@quillbrook.com
California Division of Parcel Registry 07493128
FLRB 460315

```html
<!DOCTYPE html>
<html lang="en">
<head>
<meta charset="utf-8">
<title>BLAC inc Business Card</title>
<link href="https://fonts.googleapis.com/css2?family=Ubuntu:wght@400;500;700&display=swap" rel="stylesheet">
<style>
  :root {
    --page-bg: #e9e7e3;
    --card-white: #fbfbfb;
    --card-grey: #eeeeef;
    --navy: #1b1f5e;
    --navy-deep: #10123f;
    --navy-soft: #2b3077;
    --lime: #9bc45a;
    --ink: #3a3a3c;
    --ink-soft: #6b6b70;
  }
  * { margin: 0; padding: 0; box-sizing: border-box; }
  html, body { width: 1200px; height: 1023px; overflow: hidden; }
  body {
    background: var(--page-bg);
    font-family: "Ubuntu", Arial, sans-serif;
    color: var(--ink);
    position: relative;
  }
  .card {
    position: absolute;
    left: 250px;
    width: 700px;
    height: 400px;
    border-radius: 4px;
    overflow: hidden;
    box-shadow: 0 6px 18px rgba(0,0,0,0.18);
  }
  /* Front */
  .card-front {
    top: 70px;
    background: linear-gradient(180deg, var(--card-white), var(--card-grey));
  }
  .brand {
    position: absolute;
    left: 44px;
    top: 46px;
  }
  .brand-name {
    display: flex;
    align-items: center;
    gap: 14px;
    font-size: 74px;
    font-weight: 700;
    color: var(--ink);
    line-height: 1;
    letter-spacing: 1px;
  }
  .brand-dot {
    width: 22px;
    height: 22px;
    border-radius: 50%;
    background: var(--lime);
  }
  .brand-line {
    margin-top: 8px;
    font-size: 19px;
    color: var(--navy-soft);
  }
  .person {
    position: absolute;
    left: 44px;
    top: 190px;
  }
  .person-name {
    font-size: 24px;
    font-weight: 700;
    color: var(--navy);
    text-transform: uppercase;
    letter-spacing: 0.5px;
  }
  .person-title {
    margin-top: 3px;
    font-size: 18px;
    color: var(--ink-soft);
  }
  .divider {
    position: absolute;
    left: 0;
    right: 0;
    top: 262px;
    height: 2px;
    background: var(--navy);
  }
  .contact-list {
    position: absolute;
    left: 44px;
    top: 278px;
    list-style: none;
    font-size: 17px;
    color: var(--ink);
  }
  .contact-list li {
    display: flex;
    align-items: center;
    gap: 10px;
    height: 25px;
  }
  .contact-icon {
    width: 16px;
    height: 16px;
    border-radius: 3px;
    background: var(--lime);
    display: flex;
    align-items: center;
    justify-content: center;
  }
  .license {
    position: absolute;
    left: 320px;
    top: 280px;
    font-size: 15px;
    line-height: 1.5;
    color: var(--ink);
    white-space: nowrap;
  }
  /* Back */
  .card-back {
    top: 540px;
    background: radial-gradient(circle at 35% 40%, var(--navy-soft), var(--navy) 55%, var(--navy-deep));
    display: flex;
    flex-direction: column;
    align-items: center;
    justify-content: center;
    gap: 22px;
  }
  .tagline {
    font-size: 44px;
    font-weight: 700;
    color: var(--lime);
    letter-spacing: 1px;
    text-transform: uppercase;
  }
  .web {
    font-size: 30px;
    font-weight: 700;
    color: #ffffff;
  }
</style>
</head>
<body>
  <section class="card card-front">
    <div class="brand">
      <div class="brand-name"><span class="brand-dot"></span>BLAC inc</div>
      <div class="brand-line">Brightway Lending and Capital, inc</div>
    </div>

    <div class="person">
      <div class="person-name">Marcus Delane</div>
      <div class="person-title">Mortgage Specialist</div>
    </div>

    <div class="divider"></div>

    <ul class="contact-list">
      <li><span class="contact-icon"><svg width="10" height="10" viewBox="0 0 10 10"><path d="M2 1h2l1 2-1 1c.5 1 1 1.5 2 2l1-1 2 1v2c-4 0-7-3-7-7z" fill="#fff"/></svg></span>(555)204-1187</li>
      <li><span class="contact-icon"><svg width="10" height="10" viewBox="0 0 10 10"><rect x="3" y="1" width="4" height="8" rx="1" fill="#fff"/></svg></span>(555)318-4592</li>
      <li><span class="contact-icon"><svg width="10" height="10" viewBox="0 0 10 10"><rect x="1" y="3" width="8" height="5" fill="#fff"/><rect x="3" y="1" width="4" height="2" fill="#fff"/></svg></span>(555)907-2263</li>
      <li><span class="contact-icon"><svg width="10" height="10" viewBox="0 0 10 10"><rect x="1" y="2" width="8" height="6" fill="#fff"/><path d="M1 2l4 3 4-3" stroke="#9bc45a" fill="none"/></svg></span>marcus@quillbrook.com</li>
    </ul>

    <div class="license">
      California Division of Parcel Registry 07493128<br>
      FLRB 460315
    </div>
  </section>

  <section class="card card-back">
    <div class="tagline">Let's get started</div>
    <div class="web">Quillbrook.com</div>
  </section>
</body>
</html>
```